PHD-project

i need the figures to be in the same stile. info is inside the file. There are 5 figures that need redesign. this is for PhD.

Target Market(s)

it will be used in my phd

Colors

Designer to choose colors to be used in the design.

```html
<!DOCTYPE html>
<html lang="en">
<head>
<meta charset="utf-8">
<title>Contribution Area – Venn Diagram</title>
<link href="https://fonts.googleapis.com/css2?family=Outfit:wght@500&display=swap" rel="stylesheet">
<style>
  :root {
    --bg: #ffffff;
    --circle-management: #2c759e;
    --circle-rtd: #5f99b7;
    --overlap: #135782;
    --label: #ffffff;
  }
  html, body {
    margin: 0;
    padding: 0;
    width: 1200px;
    height: 780px;
    overflow: hidden;
    background: var(--bg);
  }
  .venn-figure {
    display: block;
    width: 1200px;
    height: 780px;
  }
  .circle-management { fill: var(--circle-management); }
  .circle-rtd { fill: var(--circle-rtd); }
  .circle-overlap { fill: var(--overlap); }
  .venn-label {
    font-family: "Outfit", sans-serif;
    font-weight: 500;
    font-size: 26px;
    letter-spacing: 0.3px;
    fill: var(--label);
    text-anchor: middle;
  }
</style>
</head>
<body>
<svg class="venn-figure" viewBox="0 0 1200 780" xmlns="http://www.w3.org/2000/svg" role="img" aria-label="Venn diagram: Design Thinking in Management and Business Strategy overlapping Research Through Design, with the Contribution Area at the intersection">
  <defs>
    <clipPath id="rtd-clip">
      <circle cx="753" cy="393" r="227"/>
    </clipPath>
  </defs>

  <circle class="circle-management" cx="478" cy="393" r="227"/>
  <circle class="circle-rtd" cx="753" cy="393" r="227"/>
  <circle class="circle-overlap" cx="478" cy="393" r="227" clip-path="url(#rtd-clip)"/>

  <text class="venn-label label-management">
    <tspan x="391" y="348">Design Thinking</tspan>
    <tspan x="391" y="383">in Management</tspan>
    <tspan x="391" y="418">&amp; Business</tspan>
    <tspan x="391" y="453">Strategy</tspan>
  </text>

  <text class="venn-label label-contribution">
    <tspan x="616" y="383">Contribution</tspan>
    <tspan x="616" y="418">Area</tspan>
  </text>

  <text class="venn-label label-rtd">
    <tspan x="836" y="366">Research</tspan>
    <tspan x="836" y="401">Through Design</tspan>
    <tspan x="836" y="436">-RTD</tspan>
  </text>
</svg>
</body>
</html>
```